Flyer Design for Business: "Velvet Glow"

My Business name is "VELVET GLOW"

Laser Hair Removal
Non invasive and pain free
Look amazing and feel confident with a Hair Free body
Now is the time to start don't delay
1 treatment a month will ensure you are bikini hot for the summer months
Take full advantage of our OPENING SPECIALS of 30%-40% savings
Part payments available

CELLULITE & FAT REDUCTION
Now you too can look amazing without invasive surgery, downtime or discomfort
Tara Wellbrook & Monica Farrowdale are avid recipients of this treatment.
Effective on all skin types and delivers fast measurable results for:
Helping mums regain their pre-baby figures
Losing the love handles (but keeping the love)
Stretch mark reduction
Skin tightening
Cellulite busting on Arms, tummy, thighs.
Man boob reduction.
Latest technology:
Bi Polar radio frequency (RF)
infrared light
negative pressure (Vacuum)
Tissue manipulation through roller mechanical massage.
50% saving Call now

PDT LED REJUVENATION LIGHT THERAPY
ORVA Researchers found:
Fibroblast and muscles grew 5 times faster, stimulates
reconstruction of collagenous fibres of the dermis
These findings and more assist with:
Remove freckles, sunburn pigmentation,
Cures acne and hair follicle inflammation
Anti aging skin tightening
Reduces pore size
Improve the skin texture
Improves circulation
Red light : reduces pore size, softens skin wrinkles,reduces acne
Blue light: Kills the acne bacillus to eliminate acne, inhibit inflammation
Yellow light: Skin tightening, whitening and softens skin wrinkles
Purple light: combination of red & blue lights treats acne scars
Orange light increases cell energy and accelerates metabolism
$55 Saving and relax under the lights.

Who can resist a soothing Hot stone massage therapy after:
A hard stressful day at work
Aches and muscular pain

Pick anything from this info with a couple of nice images.

Target Market(s)

Females & males Sports minded people cyclists

Industry/Entity Type

Beauty Salon

Colors
00a990
e34197

Requirements
Must have
• a couple of images and
Nice to have
• Pink and bluey green like my business card

```html
<!DOCTYPE html>
<html lang="en">
<head>
<meta charset="utf-8">
<title>Velvet Glow Flyers</title>
<link rel="stylesheet" href="https://fonts.googleapis.com/css2?family=Lato:wght@400;700;900&display=swap">
<style>
:root{
  --pink:#e34197;
  --pink-deep:#d63a8c;
  --teal:#00a990;
  --teal-deep:#009a84;
  --white:#ffffff;
  --page:#ecebe8;
  --red:#d9352b;
  --blue:#3f62ab;
  --yellow:#f2b41c;
  --purple:#a34a9c;
  --orange:#f07a22;
}
*{box-sizing:border-box;margin:0;padding:0}
html,body{width:1200px;height:1000px;overflow:hidden}
body{background:var(--page);font-family:"Lato",sans-serif;position:relative}
.flyer{position:absolute;top:55px;width:430px;height:890px;background:var(--white);overflow:hidden;box-shadow:0 4px 14px rgba(0,0,0,.18)}
.flyer--hair{left:190px}
.flyer--massage{left:640px}
.masthead{height:118px;text-align:center;color:var(--white);padding-top:16px}
.flyer--hair .masthead{background:var(--pink)}
.flyer--massage .masthead{background:var(--teal)}
.brand-title{font-size:52px;font-weight:400;letter-spacing:.5px;line-height:1}
.web{font-size:13px;margin-top:10px}
.hero{position:relative;height:220px}
.photo{position:absolute;top:0;left:0;width:100%;height:100%}
.photo--legs{background:linear-gradient(90deg,#c99a7c 0%,#d9b29a 28%,#bfe0f4 55%,#d6ecf8 100%)}
.hero-copy{position:absolute;right:16px;top:62px;width:240px;text-align:right;color:var(--pink)}
.hero-copy h2{font-size:20px;font-weight:700;margin-bottom:10px}
.hero-copy p{font-size:12.5px;line-height:1.45}
.offer{height:90px;background:rgba(255,255,255,.92);color:var(--pink);text-align:center;font-size:18px;font-weight:700;line-height:1.3;padding-top:6px}
.call-bar{height:34px;color:var(--white);font-size:22px;font-weight:700;text-align:center;line-height:34px}
.flyer--hair .call-bar{background:var(--pink)}
.flyer--massage .call-bar{background:var(--teal)}
.light-therapy{background:var(--teal);height:360px;padding:14px 10px 0;color:var(--white)}
.light-therapy h2{font-size:19px;font-weight:700}
.light-therapy .sub{font-size:15px;margin:3px 0 6px}
.light-photos{display:flex;height:95px;margin:0 8px 6px}
.light-photos span{flex:1}
.light-photos span:first-child{flex:1.8;background:linear-gradient(135deg,#e24a3a,#f0a39a)}
.light-photos span:nth-child(2){background:linear-gradient(135deg,#4f78c2,#9db5e3)}
.light-photos span:nth-child(3){background:linear-gradient(135deg,#e3a22a,#f7d48c)}
.light-photos span:nth-child(4){background:linear-gradient(135deg,#7d3aa7,#d0a2f0)}
.light-photos span:nth-child(5){background:linear-gradient(135deg,#f08a2c,#f9c89a)}
.light-table{margin:0 8px;border-collapse:collapse;width:calc(100% - 16px)}
.light-table td{height:39.5px;font-size:10.5px;text-transform:uppercase;vertical-align:middle}
.light-table .swatch{width:130px;text-align:center;font-size:11px}
.light-table .desc{padding-left:8px;line-height:1.3}
.swatch--red{background:var(--red)}
.swatch--blue{background:var(--blue)}
.swatch--yellow{background:var(--yellow)}
.swatch--purple{background:var(--purple)}
.swatch--orange{background:var(--orange)}
.footer{height:68px;display:flex;justify-content:space-between;align-items:center;padding:0 12px 0 40px}
.footer-name{color:var(--pink);font-size:15px;font-weight:700}
.address{color:var(--pink);font-size:11px;text-align:right;line-height:1.3}
.hero--stone{height:300px}
.photo--stone{background:linear-gradient(180deg,#d8eef5 0%,#cfe3ea 40%,#b8876a 68%,#e6d3c4 100%)}
.stone-copy{position:absolute;right:12px;top:14px;width:300px;text-align:right;color:var(--teal);font-weight:700;font-size:18px;line-height:1.25}
.stone-note{position:absolute;left:10px;right:0;bottom:0;height:64px;background:rgba(255,255,255,.88);color:var(--teal);font-size:10.5px;text-transform:uppercase;line-height:1.25;padding:5px 6px 0 8px}
.cellulite{position:relative;height:382px;background:var(--pink);padding:16px 10px 0 28px;color:var(--white)}
.photo--body{left:auto;right:0;width:170px;background:linear-gradient(90deg,rgba(227,65,151,0) 0%,rgba(201,142,118,.7) 40%,#e2b49b 100%)}
.cellulite-copy{position:relative;width:300px;font-size:12.5px;line-height:1.25}
.cellulite-copy h2{font-size:19px;font-weight:700;margin-bottom:8px}
.cellulite-copy p{margin-bottom:6px}
.cellulite-copy ul{list-style:none;font-size:10.5px;text-transform:uppercase;margin-bottom:8px}
.cellulite-copy li{margin-bottom:4px}
.cellulite-copy li::before{content:"\2022\00a0"}
.tech{font-size:10.5px;text-transform:uppercase;line-height:1.2}
.saving-bar{height:56px;background:var(--pink-deep);color:var(--white);font-size:22px;font-weight:700;text-align:center;line-height:56px}
</style>
</head>
<body>
<section class="flyer flyer--hair">
  <header class="masthead">
    <h1 class="brand-title">VELVET GLOW</h1>
    <p class="web">www.velvetglow.com.au</p>
  </header>
  <div class="hero">
    <div class="photo photo--legs" role="img" aria-label="Photo of tanned legs against a bright beach sky"></div>
    <div class="hero-copy">
      <h2>Laser Hair Removal</h2>
      <p>Non invasive and pain free. Look amazing and feel confident with a Hair Free body. Now is the time to start don't delay. 1 treatment a month will ensure you are bikini hot for the summer months.</p>
    </div>
  </div>
  <div class="offer">Take full advantage of our OPENING<br>SPECIALS of 30%-40% savings !<br>Part payments available !</div>
  <div class="call-bar">Call now (02) 5550 1234</div>
  <div class="light-therapy">
    <h2>Pdt Led Rejuvenation Light Therapy</h2>
    <p class="sub">$55 Saving and relax under the lights</p>
    <div class="light-photos" role="img" aria-label="Photos of the LED therapy device glowing red, blue, yellow, purple and orange">
      <span></span><span></span><span></span><span></span><span></span>
    </div>
    <table class="light-table">
      <tr><td class="swatch swatch--red">Red light</td><td class="desc">Reduces pore size, softens skin wrinkles, reduces acne.</td></tr>
      <tr><td class="swatch swatch--blue">Blue light</td><td class="desc">Kills the acne bacillus to eliminate acne, inhibit inflammation.</td></tr>
      <tr><td class="swatch swatch--yellow">Yellow light</td><td class="desc">Skin tightening, whitening and softens skin wrinkles.</td></tr>
      <tr><td class="swatch swatch--purple">Purple light</td><td class="desc">Combination of red &amp; blue lights treats acne scars.</td></tr>
      <tr><td class="swatch swatch--orange">Orange light</td><td class="desc">Increases cell energy and accelerates metabolism.</td></tr>
    </table>
  </div>
  <footer class="footer">
    <span class="footer-name">Velvet Glow</span>
    <p class="address">4/18 Harbour Lane<br>Millbrook NSW 2999<br>For all appointments call: (02) 5550 1234<br>Mobile: 0400 555 918</p>
  </footer>
</section>

<section class="flyer flyer--massage">
  <header class="masthead">
    <h1 class="brand-title">VELVET GLOW</h1>
    <p class="web">www.velvetglow.com.au</p>
  </header>
  <div class="hero hero--stone">
    <div class="photo photo--stone" role="img" aria-label="Photo of a woman lying face down with hot stones on her back"></div>
    <p class="stone-copy">Who can resist a soothing Hot stone massage therapy after:<br>A hard stressful day at work<br>Aches and muscular pain</p>
    <p class="stone-note">Hot stone massage combines thermotherapy with massage techniques to provide an effective healing therapy. The use of natural stones in conjunction with massage uses powerful earth energies to help the patient heal.</p>
  </div>
  <div class="call-bar">Call now (02) 5550 1234</div>
  <div class="cellulite">
    <div class="photo photo--body" role="img" aria-label="Photo of a slim torso in a black bikini"></div>
    <div class="cellulite-copy">
      <h2>CELLULITE &amp; FAT REDUCTION</h2>
      <p>Now you too can look amazing without invasive surgery, downtime or discomfort.</p>
      <p>Tara Wellbrook &amp; Monica Farrowdale are avid recipients of this treatment.</p>
      <p>Effective on all skin types and delivers fast measurable results for:</p>
      <ul>
        <li>Helping mums regain their pre-baby figures</li>
        <li>Losing the love handles (but keeping the love)</li>
        <li>Stretch mark reduction</li>
        <li>Skin tightening</li>
        <li>Cellulite busting on arms, tummy, thighs.</li>
        <li>Man boob reduction</li>
      </ul>
      <p class="tech">Latest technology:<br>Bi polar radio frequency (RF)<br>Infrared light<br>Negative pressure (vacuum)<br>Tissue manipulation through roller mechanical massage.</p>
    </div>
  </div>
  <div class="saving-bar">50% saving Call now</div>
</section>
</body>
</html>
```